Halvorsen Partners Business Card

Halvorsen Partners Civil Construction
Dorian Halvorsen
CEO
555-318-4076
Dorian@HalvorsenCivil.example
www.HalvorsenCivil.example
Site Development
Utility Construction
Excavation
48730 County Route 19
Cedar Hollow 34999

Target Market(s)

Construction and government

Industry/Entity Type

Business

Contact Information for Business Card

I want an unique design that make a statement

Number of Pages Required

1 page

Font styles to use
Other font styles liked:

Colors

Designer to choose colors to be used in the design.

Requirements
Must have
• unique design, feel free to modify or change the color of my logo.
Nice to have
• extra design features like spot UV, foil accents, color edges, unique paper, or any thing that would make my card pop.
• I like the feel of the image that I attached

```html
<!DOCTYPE html>
<html lang="en">
<head>
<meta charset="utf-8">
<title>Halvorsen Partners Business Card</title>
<link href="https://fonts.googleapis.com/css2?family=Marcellus&family=Roboto+Condensed:wght@400;700&display=swap" rel="stylesheet">
<style>
  :root {
    --bg: #6b6d70;
    --night-1: #8a97ad;
    --night-2: #3c4556;
    --night-3: #0f1115;
    --navy: #2c4584;
    --navy-deep: #24396e;
    --steel: #5f6266;
    --steel-light: #7a7d82;
    --paper: #ffffff;
    --ink-light: #f2f4f8;
  }
  * { margin: 0; padding: 0; box-sizing: border-box; }
  html, body { width: 1200px; height: 907px; overflow: hidden; }
  body {
    background: var(--bg);
    font-family: "Roboto Condensed", Arial, sans-serif;
    position: relative;
  }
  .card {
    position: absolute;
    width: 640px;
    height: 366px;
    overflow: hidden;
    box-shadow: 0 12px 28px rgba(0,0,0,.35);
  }
  /* Front */
  .card-front { left: 70px; top: 60px; }
  .front-scene {
    position: absolute; inset: 0;
    background: linear-gradient(160deg, var(--night-1) 0%, var(--night-2) 55%, var(--night-3) 100%);
  }
  .front-brand {
    position: absolute; left: 90px; top: 150px;
    display: flex; align-items: center; gap: 16px;
  }
  .brand-square { width: 44px; height: 44px; background: var(--ink-light); flex: none; }
  .brand-lines { border-left: 2px solid rgba(255,255,255,.7); padding-left: 14px; }
  .brand-name {
    font-family: "Marcellus", Georgia, serif;
    font-size: 34px; letter-spacing: 1px; text-transform: uppercase;
    color: var(--ink-light); line-height: 1.05; white-space: nowrap;
  }
  .brand-sub {
    font-family: "Marcellus", Georgia, serif;
    font-size: 19px; letter-spacing: 4px; text-transform: uppercase;
    color: var(--ink-light); margin-top: 4px; white-space: nowrap;
  }
  .front-web {
    position: absolute; left: 168px; top: 250px;
    font-size: 15px; letter-spacing: 2px; color: var(--ink-light);
  }
  /* Back */
  .card-back { left: 490px; top: 480px; background: var(--paper); }
  .back-brand {
    position: absolute; left: 30px; top: 150px;
    display: flex; align-items: center; gap: 10px;
  }
  .back-brand .brand-square { width: 30px; height: 30px; background: var(--navy); }
  .back-brand .brand-lines { border-left-color: var(--steel-light); padding-left: 9px; }
  .back-brand .brand-name { font-size: 20px; letter-spacing: .5px; color: var(--navy); }
  .back-brand .brand-sub { font-size: 11px; letter-spacing: 3px; color: var(--steel); }
  .contact-panel {
    position: absolute; right: 0; top: 0; width: 290px; height: 326px;
    background: linear-gradient(180deg, var(--navy) 0%, var(--navy-deep) 100%);
  }
  .name-tab {
    position: absolute; left: 305px; top: 34px; width: 210px; height: 62px;
    background: var(--steel); color: var(--ink-light);
    padding: 10px 18px;
    clip-path: polygon(0 0, 100% 0, 92% 100%, 0 100%);
  }
  .person-name { font-size: 20px; font-weight: 700; white-space: nowrap; }
  .person-role { font-size: 12px; letter-spacing: 1px; margin-top: 2px; }
  .address {
    position: absolute; left: 380px; top: 120px;
    color: var(--ink-light); font-size: 14px; line-height: 1.4;
  }
  .contact-list {
    position: absolute; left: 380px; top: 205px; list-style: none;
    color: var(--ink-light); font-size: 14px; line-height: 1.6;
  }
  .contact-list li { display: flex; align-items: center; gap: 8px; }
  .contact-list svg { width: 12px; height: 12px; fill: var(--ink-light); flex: none; }
  .services-band {
    position: absolute; left: 0; right: 0; bottom: 0; height: 40px;
    background: var(--steel); color: var(--ink-light);
    display: flex; align-items: center; justify-content: flex-end;
    padding-right: 28px;
    font-size: 12px; font-weight: 700; letter-spacing: 1.5px; text-transform: uppercase;
  }
</style>
</head>
<body>
  <section class="card card-front">
    <div class="front-scene" role="img" aria-label="Dusk photograph of excavators silhouetted on a construction site"></div>
    <div class="front-brand">
      <span class="brand-square"></span>
      <div class="brand-lines">
        <div class="brand-name">Halvorsen Partners</div>
        <div class="brand-sub">Civil Construction</div>
      </div>
    </div>
    <div class="front-web">www.HalvorsenCivil.example</div>
  </section>

  <section class="card card-back">
    <div class="back-brand">
      <span class="brand-square"></span>
      <div class="brand-lines">
        <div class="brand-name">Halvorsen Partners</div>
        <div class="brand-sub">Civil Construction</div>
      </div>
    </div>
    <div class="contact-panel"></div>
    <div class="name-tab">
      <div class="person-name">Dorian Halvorsen</div>
      <div class="person-role">CEO</div>
    </div>
    <div class="address">48730 County Route 19<br>Cedar Hollow 34999</div>
    <ul class="contact-list">
      <li><svg viewBox="0 0 12 12"><path d="M2 1h3l1 3-1.5 1a7 7 0 0 0 2.5 2.5L8 6l3 1v3c0 .6-.4 1-1 1A9 9 0 0 1 1 2c0-.6.4-1 1-1z"/></svg>555-318-4076</li>
      <li><svg viewBox="0 0 12 12"><path d="M1 2h10v8H1z M1 2l5 4 5-4" fill="none" stroke="#f2f4f8" stroke-width="1.2"/></svg>Dorian@HalvorsenCivil.example</li>
      <li><svg viewBox="0 0 12 12"><circle cx="6" cy="6" r="5" fill="none" stroke="#f2f4f8" stroke-width="1.2"/><path d="M1 6h10M6 1c-2 3-2 7 0 10M6 1c2 3 2 7 0 10" fill="none" stroke="#f2f4f8" stroke-width="1"/></svg>www.HalvorsenCivil.example</li>
    </ul>
    <div class="services-band">Site Development • Utility Construction • Excavation</div>
  </section>
</body>
</html>
```